Golf Course hole signage

I would like to have a golf course sign created for our wealth management business. I would like to incorporate the logo branding and have my full name and role in the signage. I would also like to apply our services in the signage if possible or if size permits. We do Investment planning, financial planning, retirement planning, Tax planning and insurance planning.

My current role at the business is the following:

Marcus Pellow, QPW®, CHWA®
Associate Wealth Manager

Email: Marcus.pellow@Rvkfa.ca

Cell: 204-618-4035

Company: RK Harbour Wealth

The division of the company: RK Capital Inc.

I have also attached a photo of an older sign to give you a better idea of what the rough size would need to be!

Target Market(s)

High networth individual

Industry/Entity Type

Wealth Management

Colors
0054AA
0677BA
7BADD7
CADEEF
E8F1F8

Requirements
Nice to have
• Modern type style

```html
<!DOCTYPE html>
<html lang="en">
<head>
<meta charset="utf-8">
<title>Golf Hole Sign – RK Harbour Wealth Management</title>
<link rel="stylesheet" href="https://fonts.googleapis.com/css2?family=Inter:wght@300;400;700;800&display=swap">
<style>
  :root {
    --navy: #022b5e;
    --paper: #ffffff;
  }
  * { margin: 0; padding: 0; box-sizing: border-box; }
  html, body {
    width: 1200px;
    height: 562px;
    overflow: hidden;
    background: var(--paper);
  }
  .sign {
    position: relative;
    width: 1200px;
    height: 562px;
    background: var(--paper);
    color: var(--navy);
    font-family: "Inter", "Helvetica Neue", Arial, sans-serif;
  }
  .headline {
    position: absolute;
    top: 112px;
    left: 0;
    width: 100%;
    text-align: center;
    font-weight: 800;
    font-size: 120px;
    line-height: 118px;
    letter-spacing: 2px;
    text-transform: uppercase;
  }
  .advisor {
    position: absolute;
    left: 60px;
    top: 468px;
    width: 412px;
    text-align: center;
    line-height: 26px;
  }
  .advisor__name {
    font-weight: 700;
    font-size: 27px;
    letter-spacing: -0.2px;
  }
  .advisor__role {
    font-weight: 300;
    font-size: 26px;
    letter-spacing: -0.4px;
  }
  .contact {
    position: absolute;
    left: 520px;
    top: 468px;
    width: 354px;
    text-align: center;
    font-weight: 300;
    font-size: 26px;
    line-height: 26px;
    letter-spacing: -0.4px;
  }
  .brand {
    position: absolute;
    left: 932px;
    top: 478px;
    display: flex;
    align-items: center;
    gap: 10px;
  }
  .brand__square {
    width: 40px;
    height: 40px;
    background: var(--navy);
  }
  .brand__name {
    font-weight: 700;
    font-size: 16px;
    line-height: 17px;
    letter-spacing: 0.1px;
    text-transform: uppercase;
  }
</style>
</head>
<body>
  <main class="sign">
    <h1 class="headline">Wanna be here<br>more often?</h1>

    <section class="advisor">
      <p class="advisor__name">Marcus Pellow, QPW®, CHWA®</p>
      <p class="advisor__role">Associate Wealth Manager</p>
    </section>

    <section class="contact">
      <p class="contact__email">Marcus.pellow@Rvkfa.ca</p>
      <p class="contact__phone">204-618-4035</p>
    </section>

    <div class="brand">
      <span class="brand__square"></span>
      <p class="brand__name">RK Harbour Wealth<br>Management</p>
    </div>
  </main>
</body>
</html>
```